I would like alternative creative proposals for our website header at tumbleoakhome.com.au
The current is seen as a bit too drab and dark. We would like to liven it up a bit. The logo will remain although we are open to alternative representation or styling. All submitted designs should include a version that has the existing logo (we do use it within a black circle in other marketing).
The fundamental features of the header must be present including brand logo, search, cart etc.
We want to expand our concept of how the header could appear and function and how it represents our business. Other web site expects will be redesigned to align.
Please become familiar with our business and what we are trying to achieve before submitting a design. We are about health, organic products, chemical free low toxin living, environmental sustainability, all delivered in a modern socially friendly way accessible to all demographics and walks of life with our primary focus on Australia. Our primary target demographic is Australian women between 35 and 55. If you would like more info then please send us some questions.
Development and full design is outside the scoop of this proposal. We are looking for "mockup" proposals for the new website header initially.

```html
<!DOCTYPE html>
<html lang="en">
<head>
<meta charset="utf-8">
<title>Tumble Oak Home — Header</title>
<link href="https://fonts.googleapis.com/css2?family=Noto+Sans:wght@400;500&display=swap" rel="stylesheet">
<style>
  :root {
    --teal: #0fa98f;
    --slate: #a2a7ac;
    --paper: #f2f2f2;
    --ink: #111111;
    --coral: #ee5a52;
    --caret: #9a9ea3;
    --leaf: #14a88e;
  }
  * { box-sizing: border-box; margin: 0; padding: 0; }
  html, body {
    width: 1200px; height: 240px; overflow: hidden;
    background: var(--paper);
    font-family: "Noto Sans", Verdana, sans-serif;
    color: var(--ink);
  }
  .site-header { width: 1200px; height: 240px; position: relative; }

  .utility-bar {
    height: 44px; background: var(--teal);
    display: flex; justify-content: flex-end; align-items: center;
    gap: 20px; padding-right: 32px; font-size: 19px;
  }
  .utility-bar a { display: flex; align-items: center; gap: 2px; color: var(--ink); text-decoration: none; }
  .utility-bar svg { display: block; }

  .account-bar {
    height: 44px; background: var(--slate);
    display: flex; justify-content: flex-end; align-items: center;
    gap: 36px; padding-right: 32px; font-size: 19px; letter-spacing: 0.2px;
  }
  .account-bar a { color: var(--ink); text-decoration: none; }

  .brand-row { position: relative; height: 100px; }
  .brand {
    position: absolute; left: 22px; top: 12px;
    display: flex; align-items: center; gap: 18px;
    text-decoration: none; color: var(--ink);
  }
  .brand-dot { width: 62px; height: 62px; border-radius: 50%; background: var(--leaf); }
  .brand-name { font-size: 44px; font-weight: 400; letter-spacing: 0.3px; line-height: 1; }

  .search {
    position: absolute; left: 878px; top: 104px; width: 290px;
    display: flex; justify-content: space-between; align-items: center;
    border-bottom: 6px solid var(--ink); padding-bottom: 10px;
  }
  .search-field { font-size: 19px; color: var(--ink); }
  .search-button { display: block; margin-top: -6px; }

  .category-nav {
    position: absolute; left: 21px; right: 30px; top: 194px;
    display: flex; justify-content: space-between; font-size: 16.5px;
  }
  .category-nav a { color: var(--ink); text-decoration: none; display: flex; align-items: center; gap: 3px; }
  .category-nav a::after {
    content: ""; width: 0; height: 0;
    border-left: 6px solid transparent; border-right: 6px solid transparent;
    border-top: 10px solid var(--caret); margin-top: 3px;
  }
</style>
</head>
<body>
<header class="site-header">
  <div class="utility-bar">
    <a href="#" class="compare-link">
      <svg width="24" height="24" viewBox="0 0 24 24" aria-hidden="true">
        <g stroke="var(--coral)" stroke-width="3" fill="none" stroke-linecap="round">
          <line x1="2" y1="22" x2="10" y2="14"/><polyline points="5,14 10,14 10,19"/>
          <line x1="22" y1="2" x2="14" y2="10"/><polyline points="19,10 14,10 14,5"/>
        </g>
      </svg>
      Compare
    </a>
    <a href="#" class="wishlist-link">
      <svg width="28" height="26" viewBox="0 0 28 26" aria-hidden="true">
        <path d="M14 25 C6 18 1 13 1 7.5 C1 3.5 4 1 7.5 1 C10.5 1 12.5 3 14 5 C15.5 3 17.5 1 20.5 1 C24 1 27 3.5 27 7.5 C27 13 22 18 14 25 Z" fill="var(--coral)"/>
      </svg>
      (0)
    </a>
    <a href="#" class="cart-link">&nbsp;My Cart (0)</a>
  </div>

  <nav class="account-bar">
    <a href="#">MY ACCOUNT</a>
    <a href="#">BLOG</a>
    <a href="#">LOG IN</a>
    <a href="#">JOIN</a>
  </nav>

  <div class="brand-row">
    <a href="#" class="brand">
      <span class="brand-dot" aria-hidden="true"></span>
      <span class="brand-name">tumble oak home</span>
    </a>
  </div>

  <form class="search" role="search">
    <span class="search-field">Search for a product...</span>
    <svg class="search-button" width="30" height="26" viewBox="0 0 30 26" aria-label="Search">
      <circle cx="10" cy="10" r="7.5" fill="none" stroke="var(--ink)" stroke-width="3.5"/>
      <line x1="16" y1="15" x2="28" y2="24" stroke="var(--ink)" stroke-width="5" stroke-linecap="round"/>
    </svg>
  </form>

  <nav class="category-nav">
    <a href="#">Fresh</a>
    <a href="#">Food &amp; Drink</a>
    <a href="#">Health &amp; Hygiene</a>
    <a href="#">Skin, Hair &amp; Body</a>
    <a href="#">Mum &amp; Bub</a>
    <a href="#">Yoga &amp; Wellbeing</a>
    <a href="#">Eco Toxin Free Living</a>
    <a href="#">Eco Clothing</a>
  </nav>
</header>
</body>
</html>
```